Label

I need a label designed for a bottle of water. I like the lightning bolt and the blue. But I do not want it exactly like the Zimm-ooh.

The label needs to be 9 inches by 2.5 inches.

Logo Text

Mesa Spring: Sip the Mesa

```html
<!DOCTYPE html>
<html lang="en">
<head>
<meta charset="utf-8">
<title>Mesa Spring – Bottle Label</title>
<link rel="stylesheet" href="https://fonts.googleapis.com/css2?family=Arimo:wght@400;700&display=swap">
<style>
  :root {
    --page: #ffffff;
    --sky-top: #0b1c2e;
    --sky-mid: #0a4f86;
    --sky-low: #0a78c2;
    --sky-glow: #8fd0ee;
    --bolt-light: rgba(235, 245, 255, 0.55);
    --ink: #0e1430;
    --white: #ffffff;
  }
  * { margin: 0; padding: 0; box-sizing: border-box; }
  html, body {
    width: 1200px;
    height: 438px;
    overflow: hidden;
    background: var(--page);
    font-family: "Arimo", Arial, sans-serif;
  }
  .canvas {
    position: relative;
    width: 1200px;
    height: 438px;
  }
  .label {
    position: absolute;
    left: 75px;
    top: 77px;
    width: 1040px;
    height: 289px;
    overflow: hidden;
    background: linear-gradient(to bottom,
      var(--sky-top) 0%,
      var(--sky-mid) 45%,
      var(--sky-low) 85%,
      var(--sky-glow) 100%);
  }
  .lightning-art {
    position: absolute;
    left: 340px;
    top: 0;
    width: 240px;
    height: 289px;
    background: radial-gradient(ellipse 50% 60% at 50% 45%,
      var(--bolt-light) 0%,
      rgba(235, 245, 255, 0.18) 55%,
      rgba(235, 245, 255, 0) 100%);
  }
  .brand-name {
    position: absolute;
    left: 0;
    right: 0;
    top: 62px;
    text-align: center;
    font-weight: 700;
    font-size: 72px;
    line-height: 1;
    letter-spacing: -1px;
    color: var(--white);
  }
  .tagline {
    position: absolute;
    left: 243px;
    top: 191px;
    width: 530px;
    height: 58px;
    border-radius: 14px;
    background: var(--white);
    color: var(--ink);
    font-weight: 400;
    font-size: 46px;
    line-height: 58px;
    text-align: center;
  }
  .volume {
    position: absolute;
    left: 0;
    right: 0;
    top: 265px;
    padding-left: 24px;
    text-align: center;
    font-weight: 700;
    font-size: 10px;
    color: var(--ink);
  }
</style>
</head>
<body>
  <main class="canvas">
    <section class="label">
      <div class="lightning-art" role="img" aria-label="Forked white lightning bolts striking down through the blue sky"></div>
      <h1 class="brand-name">Mesa Spring</h1>
      <p class="tagline">Sip the Mesa</p>
      <p class="volume">1 Liter</p>
    </section>
  </main>
</body>
</html>
```